Bold & Clean Brisk Harbor Stationary Design

Our company, Brisk Harbor Capital Partners needs a business card, letterhead, and envelope design that all also the formatting standards for quickleafpress.com.

Envelope:
Safe Zone: 9.375" x 4"
Trim Size: 9.5" x 4.15"
Bleed Size: 11.125" 8.625"

Letterhead:
Safe Zone: 10.875" x 8.375"
Trim Size: 11" x 8.5"
Bleed Size: 11.125" x 8.625"

Our mailing address is:
2870 W Larkhill St
Chicago, IL 60618

Please make sure the return address on the envelope is formatted correctly for mailing and the logo is not too large.

Please submit designs in word and PDF form.

Our current letterhead is attached.

We would also like a business card with our existing logo that will meet standards for formatting through Quickleaf Press (quickleafpress.com).

These standards are:
Safe Zone: 3.375" x 1.875"
Trim Size: 3.5" x 2"
Bleed Size: 3.625" x 2.125"

The business card is going to be for Marco Lindqvist, President/CEO of Brisk Harbor Capital Partners. Please include the Address, Telephone Number, Cell Phone Number, Fax Number, Email, and Website Address on the card, which are as follows:

2870 W Larkhill St
Chicago, IL 60618

Tel: (773) 555-0172
Cell: (630) 555-0138
Fax: (63) 555-0194
Email: mrl@briskharborcap.com
Web: www.briskharborcap.com

Please make sure that we can easily change the name of the staff member and job position title ourselves as we will be having cards for individual employees in the future as well.

The back of the card should also have the Brisk Harbor logo on it with our services listed:

Financial Planning | Tax | Solutions for Small Businesses

Industry/Entity Type

Accounting

Requirements
Must have
• envelope
• letterhead
• business card
• All meeting standards set out above.

```html
<!DOCTYPE html>
<html lang="en">
<head>
<meta charset="utf-8">
<title>Brisk Harbor Capital Partners – Stationery</title>
<link href="https://fonts.googleapis.com/css2?family=Open+Sans:wght@400;600;700&display=swap" rel="stylesheet">
<style>
  :root{
    --navy:#233a5e;
    --orange:#f05a28;
    --ink:#3a3a3a;
    --muted:#6b6b6b;
    --paper:#ffffff;
    --backdrop:#ececec;
  }
  *{box-sizing:border-box;margin:0;padding:0}
  html,body{width:1200px;height:937px;overflow:hidden}
  body{background:var(--backdrop);font-family:"Open Sans",Arial,sans-serif;color:var(--ink);position:relative}
  .sheet{position:absolute;background:var(--paper);overflow:hidden}

  /* brand lockup */
  .brand{display:flex;align-items:center;color:var(--navy);font-weight:700;line-height:1.05;letter-spacing:.02em}
  .brand-dot{border-radius:50%;background:var(--orange);flex:none}
  .brand-name{white-space:nowrap}

  /* letterhead */
  .letterhead{left:185px;top:68px;width:388px;height:544px}
  .letterhead .brand{position:absolute;left:20px;top:22px;gap:8px;font-size:12px}
  .letterhead .brand-dot{width:30px;height:30px}
  .letterhead-contact{position:absolute;right:18px;top:22px;text-align:right;font-size:5.5px;line-height:1.5;color:var(--muted)}
  .letter{position:absolute;left:36px;top:138px;width:300px;font-size:5.2px;line-height:1.55;color:var(--ink)}
  .letter p{margin-bottom:9px}
  .letter .date{margin-bottom:8px}
  .letter .greeting{margin-bottom:6px}
  .letter strong{font-weight:700}
  .signature{width:36px;height:18px;background:linear-gradient(90deg,#d5d5d5,#bdbdbd);border-radius:3px;margin:4px 0 6px}

  /* presentation sheet */
  .cover{left:636px;top:41px;width:459px;height:575px}
  .cover .brand{position:absolute;left:62px;top:283px;gap:18px;font-size:28px}
  .cover .brand-dot{width:78px;height:78px}

  /* business card */
  .card-front{left:46px;top:658px;width:176px;height:100px}
  .card-front .brand{position:absolute;left:8px;top:10px;gap:4px;font-size:6.5px}
  .card-front .brand-dot{width:16px;height:16px}
  .card-person{position:absolute;right:10px;top:47px;text-align:right;font-size:6px;line-height:1.3}
  .card-person .name{font-weight:700;color:var(--navy)}
  .card-details{position:absolute;left:8px;bottom:8px;font-size:3.6px;line-height:1.45;color:var(--muted)}
  .card-web{position:absolute;right:10px;bottom:8px;font-size:4.2px;letter-spacing:.12em;color:var(--muted)}
  .card-back{left:46px;top:785px;width:176px;height:99px}
  .card-back .brand{position:absolute;left:34px;top:32px;gap:5px;font-size:7.5px}
  .card-back .brand-dot{width:22px;height:22px}
  .card-services{position:absolute;left:0;right:0;top:66px;text-align:center;font-size:4.2px;letter-spacing:.06em;color:var(--muted);white-space:nowrap}

  /* envelope */
  .envelope-front{left:265px;top:674px;width:431px;height:206px}
  .envelope-front .brand{position:absolute;left:16px;top:20px;gap:10px;font-size:13px}
  .envelope-front .brand-dot{width:40px;height:40px}
  .return-address{position:absolute;left:66px;top:64px;font-size:6.5px;line-height:1.45;color:var(--muted)}
  .envelope-back{left:737px;top:672px;width:431px;height:207px}
  .flap{position:absolute;left:0;top:0;width:100%;height:72px;background:var(--orange);border-radius:0 0 40px 40px}
  .flap-web{position:absolute;left:0;right:0;top:32px;text-align:center;color:#fff;font-size:9px;letter-spacing:.3em}
  .flap-web b{font-weight:700}
</style>
</head>
<body>

<section class="sheet letterhead">
  <div class="brand"><span class="brand-dot"></span><span class="brand-name">Brisk Harbor<br>Capital Partners</span></div>
  <div class="letterhead-contact">
    2870 W Larkhill St<br>Chicago, IL 60618<br>(773) 555-0172<br>mrl@briskharborcap.com
  </div>
  <div class="letter">
    <p class="date">July 2, 2012</p>
    <p class="greeting"><strong>Dear Client,</strong><br>14 Alder Court, Suite 2, Chicago IL</p>
    <p>Thank you for choosing our firm for your planning needs this year. We have reviewed the documents you shared and prepared a short summary of next steps for your household accounts. Our team will contact you within the week to confirm a meeting time that suits your schedule. In the meantime, please gather recent statements, prior tax returns and any notes on goals you would like us to consider. We look forward to working with you.</p>
    <p>Our advisors are available by phone or email for any questions before the meeting, and we are glad to help.</p>
    <p style="margin-top:16px">Please note that our office hours change during the filing season. We will send a reminder before each deadline so that nothing is missed. If your business has new staff, equipment or income sources, let us know early so we can plan for them. We value the trust you place in us and aim to keep every step simple, clear and on time for you and your family.</p>
    <p style="margin-bottom:2px">Best Regards,</p>
    <div class="signature" role="img" aria-label="Handwritten signature"></div>
    <p><strong>Helena Brandt</strong><br>Director<br><br>14 Alder Court, Suite 2, Chicago IL</p>
  </div>
</section>

<section class="sheet cover">
  <div class="brand"><span class="brand-dot"></span><span class="brand-name">Brisk Harbor<br>Capital Partners</span></div>
</section>

<section class="sheet card-front">
  <div class="brand"><span class="brand-dot"></span><span class="brand-name">Brisk Harbor<br>Capital Partners</span></div>
  <div class="card-person"><div class="name">Marco Lindqvist</div><div>President/CEO</div></div>
  <div class="card-details">
    Tel: (773) 555-0172<br>mrl@briskharborcap.com<br>2870 W Larkhill St, Chicago, IL 60618
  </div>
  <div class="card-web">www.briskharborcap.com</div>
</section>

<section class="sheet card-back">
  <div class="brand"><span class="brand-dot"></span><span class="brand-name">Brisk Harbor<br>Capital Partners</span></div>
  <div class="card-services">Financial Planning | Tax | Solutions for Small Businesses</div>
</section>

<section class="sheet envelope-front">
  <div class="brand"><span class="brand-dot"></span><span class="brand-name">Brisk Harbor<br>Capital Partners</span></div>
  <div class="return-address">2870 W Larkhill St<br>Chicago, IL 60618</div>
</section>

<section class="sheet envelope-back">
  <div class="flap"><div class="flap-web">www.<b>briskharborcap</b>.com</div></div>
</section>

</body>
</html>
```